Brightmere Facebook Design

Build out a really nice and professional Facebook Page and full banner for Brightmere perhaps with the our services portfolio across the page as well,
Pls check www.brightmere-example.com.au for ideas to a make the Facebook Page look professional like a similar theme to our website and the porfolio of services

Main photo please emphasis the equipment cleaning and the gurney cleaning a lower priority to emphasize is the general cleaning
Thanks very much

Target Market(s)

Restaurant, warehouses, factories, car and fleet companies, hotels and buffets, chain restaurants, pizza huts, burger eateries, leisure centres

Industry/Entity Type

Cleaning Services

Font styles to use
Serif

Colors
3277b5
f04a50
f37122
fcf299
ec1f27

Requirements
Must have
• Energy and professional Facebook Site with some of the Brightmere Flowers across it and the portfolio of services
Nice to have
• Good vibrant colours

Professional similar to the website

```html
<!DOCTYPE html>
<html lang="en">
<head>
<meta charset="utf-8">
<title>Brightmere Facebook Banners</title>
<link rel="stylesheet" href="https://fonts.googleapis.com/css2?family=Tinos:wght@400;700&family=Roboto:wght@400;500&display=swap">
<style>
  :root {
    --stage-grey: #a3a3a3;
    --panel-grey: #efefef;
    --navy: #1f4f8c;
    --navy-deep: #173f74;
    --brand-blue: #3277b5;
    --orange: #fb5a0b;
    --orange-soft: #f37122;
    --white: #ffffff;
    --logo-navy: #1d3f73;
  }
  * { box-sizing: border-box; margin: 0; padding: 0; }
  html, body {
    width: 1031px; height: 1200px; overflow: hidden;
    background: var(--stage-grey);
  }
  .stage {
    position: absolute; left: 0; top: 0;
    width: 930px; height: 1082px;
    transform: scale(1.1086); transform-origin: 0 0;
  }
  .banner {
    position: absolute; left: 54px;
    width: 820px; height: 477px;
    background: var(--panel-grey);
    overflow: hidden;
  }
  .banner--strips { top: 42px; }
  .banner--tiles { top: 549px; }
  .banner-art { position: absolute; left: 0; top: 0; width: 820px; height: 360px; }
  .heading {
    position: absolute; left: 36px;
    font-family: "Tinos", "Times New Roman", serif; font-weight: 700;
    font-size: 17px; color: var(--white); letter-spacing: 0.2px;
  }
  .heading--career { top: 22px; }
  .heading--testimonials { top: 141px; }
  .job { position: absolute; top: 56px; width: 160px; color: var(--white); font-family: "Roboto", Arial, sans-serif; }
  .job--one { left: 35px; }
  .job--two { left: 210px; }
  .job-title { font-size: 14px; font-weight: 500; }
  .job-text { margin-top: 6px; font-size: 9.5px; line-height: 12px; }
  .client-badge {
    position: absolute; left: 39px; top: 178px; width: 131px; height: 61px;
    background: var(--white); border-radius: 3px;
    display: flex; align-items: center; justify-content: center;
    font-family: "Tinos", "Times New Roman", serif; font-weight: 700;
    font-size: 20px; color: var(--navy);
  }
  .testimonial {
    position: absolute; top: 179px; width: 172px;
    font-family: "Roboto", Arial, sans-serif; font-size: 12px; line-height: 17px;
    color: var(--white);
  }
  .banner--strips .testimonial { left: 187px; }
  .banner--tiles .testimonial { left: 196px; }
  .brand-disc {
    position: absolute; left: 35px; top: 276px; width: 178px; height: 178px;
    border-radius: 50%; background: var(--white);
    display: flex; flex-direction: column; align-items: center; justify-content: center;
  }
  .brand-dot { width: 34px; height: 34px; border-radius: 50%; background: var(--logo-navy); margin-bottom: 12px; }
  .brand-name {
    font-family: "Tinos", "Times New Roman", serif; font-weight: 400;
    font-size: 29px; color: var(--logo-navy);
  }
  .service-label {
    position: absolute; font-family: "Tinos", "Times New Roman", serif; font-weight: 700;
    color: var(--white); font-size: 16.5px; line-height: 25px; text-transform: uppercase;
  }
  .banner--strips .service-label { right: 24px; text-align: right; }
  .banner--tiles .service-label { font-size: 15px; line-height: 20px; }
</style>
</head>
<body>
<div class="stage">

  <section class="banner banner--strips">
    <svg class="banner-art" viewBox="0 0 820 360">
      <defs>
        <linearGradient id="office-a" x1="0" y1="0" x2="1" y2="1">
          <stop offset="0" stop-color="#2c5e9c"/><stop offset="1" stop-color="#1b4580"/>
        </linearGradient>
        <linearGradient id="strip-navy" x1="0" x2="1">
          <stop offset="0" stop-color="#9aa6b4"/><stop offset="0.55" stop-color="#2f5890"/><stop offset="1" stop-color="#1b4a86"/>
        </linearGradient>
        <linearGradient id="strip-orange" x1="0" x2="1">
          <stop offset="0" stop-color="#d9d4cf"/><stop offset="0.5" stop-color="#f07a36"/><stop offset="1" stop-color="#fb5a0b"/>
        </linearGradient>
        <linearGradient id="strip-deck" x1="0" x2="1">
          <stop offset="0" stop-color="#5a3d2a"/><stop offset="0.5" stop-color="#e0682a"/><stop offset="1" stop-color="#fb5a0b"/>
        </linearGradient>
        <clipPath id="right-area-a">
          <path d="M341,0 C395,50 410,120 420,190 C430,260 450,320 488,360 L820,360 L820,0 Z"/>
        </clipPath>
      </defs>
      <rect width="820" height="360" fill="url(#office-a)" role="img" aria-label="Photo of office cleaners at work, tinted blue"/>
      <g clip-path="url(#right-area-a)">
        <rect x="0" y="0" width="820" height="90" fill="url(#strip-navy)" role="img" aria-label="Photo of equipment being serviced"/>
        <rect x="0" y="90" width="820" height="90" fill="url(#strip-orange)" role="img" aria-label="Photo of kitchen oven being cleaned"/>
        <rect x="0" y="180" width="820" height="90" fill="url(#strip-navy)" role="img" aria-label="Photo of office surface being wiped"/>
        <rect x="0" y="270" width="820" height="90" fill="url(#strip-deck)" role="img" aria-label="Photo of deck under a high pressure washer"/>
        <line x1="0" y1="90" x2="820" y2="90" stroke="#ffffff" stroke-width="1.5"/>
        <line x1="0" y1="180" x2="820" y2="180" stroke="#ffffff" stroke-width="1.5"/>
        <line x1="0" y1="270" x2="820" y2="270" stroke="#ffffff" stroke-width="1.5"/>
      </g>
      <path d="M341,0 C395,50 410,120 420,190 C430,260 450,320 488,360" fill="none" stroke="#ffffff" stroke-width="9"/>
      <circle cx="410" cy="169" r="34" fill="#ffffff"/>
      <circle cx="410" cy="169" r="19" fill="#1d3f73"/>
    </svg>

    <h2 class="heading heading--career">CAREER INFORMATION</h2>
    <div class="job job--one"><p class="job-title">Job Title here</p><p class="job-text">Augiat in pede Fusce tellus Sed metus augue convallis</p></div>
    <div class="job job--two"><p class="job-title">Job Title here</p><p class="job-text">Augiat in pede Fusce tellus Sed metus augue convallis</p></div>
    <h2 class="heading heading--testimonials">TESTIMONIALS</h2>
    <div class="client-badge">Crestway</div>
    <p class="testimonial">We successfully managed the<br>roll out of 200 equipment asset<br>frost blender Machines</p>

    <p class="service-label" style="top:16px">Equipment<br>Services</p>
    <p class="service-label" style="top:110px">Kitchen<br>Detail Clean</p>
    <p class="service-label" style="top:194px">General<br>Office&nbsp; Cleaning</p>
    <p class="service-label" style="top:294px">High Pressure<br>Cleaning</p>

    <div class="brand-disc"><span class="brand-dot"></span><span class="brand-name">Brightmere</span></div>
  </section>

  <section class="banner banner--tiles">
    <svg class="banner-art" viewBox="0 0 820 360">
      <defs>
        <linearGradient id="office-b" x1="0" y1="0" x2="1" y2="1">
          <stop offset="0" stop-color="#2c5e9c"/><stop offset="1" stop-color="#1b4580"/>
        </linearGradient>
        <linearGradient id="tile-equip" x1="0" y1="0" x2="1" y2="1">
          <stop offset="0" stop-color="#8c8f93"/><stop offset="1" stop-color="#2a2c30"/>
        </linearGradient>
        <linearGradient id="tile-kitchen" x1="0" y1="0" x2="1" y2="1">
          <stop offset="0" stop-color="#6b6b6b"/><stop offset="0.6" stop-color="#4a4845"/><stop offset="1" stop-color="#c9a920"/>
        </linearGradient>
        <linearGradient id="tile-pressure" x1="0" y1="0" x2="0" y2="1">
          <stop offset="0" stop-color="#4f6b3a"/><stop offset="1" stop-color="#8a8a86"/>
        </linearGradient>
        <linearGradient id="tile-office" x1="0" y1="0" x2="1" y2="1">
          <stop offset="0" stop-color="#6f7176"/><stop offset="1" stop-color="#a9abb0"/>
        </linearGradient>
        <clipPath id="right-area-b">
          <path d="M341,0 C395,50 410,120 420,190 C430,260 450,320 488,360 L820,360 L820,0 Z"/>
        </clipPath>
      </defs>
      <rect width="820" height="360" fill="url(#office-b)" role="img" aria-label="Photo of office cleaners at work, tinted blue"/>
      <rect width="820" height="360" fill="#fb5a0b" clip-path="url(#right-area-b)"/>
      <path d="M341,0 C395,50 410,120 420,190 C430,260 450,320 488,360" fill="none" stroke="#ffffff" stroke-width="9"/>
      <rect x="457" y="29" width="167" height="143" rx="42" fill="url(#tile-equip)" role="img" aria-label="Photo of equipment being wiped down"/>
      <rect x="633" y="29" width="166" height="143" rx="42" fill="url(#tile-kitchen)" role="img" aria-label="Photo of gloved hand cleaning a stove"/>
      <rect x="457" y="180" width="167" height="140" rx="42" fill="url(#tile-pressure)" role="img" aria-label="Photo of pressure washing outdoors"/>
      <rect x="633" y="180" width="166" height="140" rx="42" fill="url(#tile-office)" role="img" aria-label="Photo of office desk being wiped"/>
      <circle cx="630" cy="177" r="21" fill="#ffffff"/>
      <circle cx="630" cy="177" r="12" fill="#1d3f73"/>
      <circle cx="410" cy="169" r="34" fill="#ffffff"/>
      <circle cx="410" cy="169" r="19" fill="#1d3f73"/>
    </svg>

    <h2 class="heading heading--career">CAREER INFORMATION</h2>
    <div class="job job--one"><p class="job-title">Job Title here</p><p class="job-text">Augiat in pede Fusce tellus Sed metus augue convallis</p></div>
    <div class="job job--two"><p class="job-title">Job Title here</p><p class="job-text">Augiat in pede Fusce tellus Sed metus augue convallis</p></div>
    <h2 class="heading heading--testimonials">TESTIMONIALS</h2>
    <div class="client-badge">Crestway</div>
    <p class="testimonial">We successfully managed the<br>roll out of 200 equipment asset<br>frost blender Machines</p>

    <p class="service-label" style="left:496px;top:120px">Equipment<br>Services</p>
    <p class="service-label" style="left:652px;top:120px">Kitchen<br>Detail Clean</p>
    <p class="service-label" style="left:491px;top:244px">High<br>Pressure<br>Cleaning</p>
    <p class="service-label" style="left:662px;top:247px">General<br>Office<br>Cleaning</p>

    <div class="brand-disc"><span class="brand-dot"></span><span class="brand-name">Brightmere</span></div>
  </section>

</div>
</body>
</html>
```